Local Flower Farm Needs Business Card Design

I need business cards designed for a flower farm based in Eudora, Kansas.
Business Info:
We are a local cut flower farm located in Eudora, Kansas, founded by Darla Whitcombe. What started as a passion for agriculture and search for more joy in daily life has blossomed into a small business dedicated to providing the community with beautiful, fresh, and sustainable flowers. We specialize in local, seasonal blooms, ensuring that every petal reflects the care and dedication we pour into our craft. Our mission is to deliver the highest quality flowers directly to our customers through local farmers markets and to florists who share our commitment to sustainability. Join us in celebrating the beauty of nature, one bloom at a time!
Contact Details:
Darla Whitcombe
Owner
Phone 913-555-0148
Facebook: Rosalind Pike Gardens
Instagram: @RosalindPikeGardens
Website: RosalindPikeGardens.example
Target Market(s)
Wholesale to Florists and Direct to Consumer via Farmers Market
Industry/Entity Type
Florist, Farm
Contact Information for Business Card
Name, Contact Info, Logo
Look and feel
Each slider illustrates characteristics of the customer's brand and the style your logo design should communicate.

```html
<!DOCTYPE html>
<html lang="en">
<head>
<meta charset="utf-8">
<title>Rosalind Pike Gardens — Business Card</title>
<link href="https://fonts.googleapis.com/css2?family=Libre+Caslon+Text:wght@400;700&display=swap" rel="stylesheet">
<style>
  :root {
    --stage: #2a2c2f;
    --teal-deep: #08212a;
    --teal: #0c3037;
    --teal-soft: #164149;
    --paper: #ffffff;
    --ink: #0d2a30;
    --muted: #5a5f62;
    --rule: #8a8f92;
  }
  * { box-sizing: border-box; margin: 0; padding: 0; }
  html, body { width: 1200px; height: 840px; overflow: hidden; }
  body {
    background: var(--stage);
    font-family: "Libre Caslon Text", Georgia, serif;
    position: relative;
  }
  .card {
    position: absolute;
    width: 520px;
    height: 300px;
    border-radius: 22px;
    overflow: hidden;
    box-shadow: 0 14px 30px rgba(0,0,0,.45);
  }
  .card--front {
    left: 70px; top: 110px;
    background: linear-gradient(115deg, var(--teal-deep) 0%, var(--teal) 55%, var(--teal-soft) 100%);
  }
  .card--back {
    left: 610px; top: 430px;
    background: var(--paper);
  }
  .brand-seal {
    position: absolute;
    border-radius: 50%;
    display: flex;
    align-items: center;
    justify-content: center;
    text-align: center;
    font-weight: 400;
    text-transform: uppercase;
    letter-spacing: .12em;
    line-height: 1.5;
  }
  .card--front .brand-seal {
    left: 70px; top: 45px;
    width: 210px; height: 210px;
    border: 1.5px solid var(--paper);
    color: var(--paper);
    font-size: 17px;
  }
  .card--back .brand-seal {
    left: 232px; top: 22px;
    width: 128px; height: 128px;
    border: 1px solid var(--ink);
    color: var(--ink);
    font-size: 11px;
  }
  .holder {
    position: absolute;
    left: 36px; top: 196px;
    width: 230px;
    text-align: right;
  }
  .holder__name {
    font-weight: 700;
    font-size: 19px;
    letter-spacing: .02em;
    color: var(--ink);
    text-transform: uppercase;
  }
  .holder__role {
    font-size: 13px;
    color: var(--muted);
    margin-top: 2px;
  }
  .divider {
    position: absolute;
    left: 282px; top: 168px;
    width: 1px; height: 100px;
    background: var(--rule);
  }
  .contact-list {
    position: absolute;
    left: 294px; top: 170px;
    list-style: none;
  }
  .contact-list li {
    display: flex;
    align-items: center;
    gap: 8px;
    height: 24px;
    font-size: 12.5px;
    color: var(--muted);
    white-space: nowrap;
  }
  .contact-icon { width: 14px; height: 14px; flex: none; }
</style>
</head>
<body>
  <section class="card card--front" aria-label="Card front">
    <div class="brand-seal">Rosalind<br>Pike<br>Gardens</div>
  </section>

  <section class="card card--back" aria-label="Card back">
    <div class="brand-seal">Rosalind<br>Pike<br>Gardens</div>

    <div class="holder">
      <p class="holder__name">Darla Whitcombe</p>
      <p class="holder__role">Owner</p>
    </div>

    <div class="divider"></div>

    <ul class="contact-list">
      <li>
        <svg class="contact-icon" viewBox="0 0 14 14" aria-hidden="true">
          <path d="M3 1.5 L5 1.5 L6 4.2 L4.6 5.2 Q5.6 7.8 8.8 9.4 L9.8 8 L12.5 9 L12.5 11 Q12.5 12.5 11 12.5 Q2 12 1.5 3 Q1.5 1.5 3 1.5 Z" fill="var(--ink)"/>
        </svg>
        913-555-0148
      </li>
      <li>
        <svg class="contact-icon" viewBox="0 0 14 14" aria-hidden="true"><circle cx="7" cy="7" r="6" fill="var(--ink)"/></svg>
        Rosalind Pike Gardens
      </li>
      <li>
        <svg class="contact-icon" viewBox="0 0 14 14" aria-hidden="true"><rect x="1" y="1" width="12" height="12" rx="2" fill="var(--ink)"/></svg>
        @RosalindPikeGardens
      </li>
      <li>
        <svg class="contact-icon" viewBox="0 0 14 14" aria-hidden="true">
          <circle cx="7" cy="7" r="6" fill="none" stroke="var(--ink)" stroke-width="1.4"/>
          <ellipse cx="7" cy="7" rx="2.6" ry="6" fill="none" stroke="var(--ink)" stroke-width="1.2"/>
          <line x1="1" y1="7" x2="13" y2="7" stroke="var(--ink)" stroke-width="1.2"/>
        </svg>
        RosalindPikeGardens.example
      </li>
    </ul>
  </section>
</body>
</html>
```